Asia based real estate financing firm needs and AWESOME design for a biz card -Harbor Lending Circle

Looking for a stylish, & corporate-looking business card for a real estate financing brokerage firm in Asia, offering global mortgage loans. I uploaded our current logos. We would like to add a splash of color (perhaps the house icon) or any other suggestions are open. For the winning designer, we have a lot of work! Thanks and best of luck!

Target Market(s)

Real estate investors globally. We want to look more like a BANK and NOT a real estate company. Please don't play up on a "house" design.

Industry/Entity Type

Banking

Contact Information for Business Card

Harbor Lending Circle
Peter Wilks
Co-Founder | Partner

14 Cassia Lane, Suite 310
Singapore 047219
www.hlc-example.asia
peterwilks@hlc-example.asia
+65 555-0142
WeChat: peterwilks

Colors

Designer to choose colors to be used in the design.

Requirements
Must have
• Must have the standard business requirements for a card; name, address, email, etc
• Can be horizontal or vertical.
Nice to have
• It would be great to see some sort of variation to the logo with a pop of color. Red is good as we're in Asia, however, other options work as well.
• Our tag line is - Borderless mortgages. It doesn't have to be on the card but might be nice.
• I'd like to start seeing our tagline within the cards as well. - Borderless mortgages.
• Also, please add our location. The location for this card is Singapore so perhaps it can be highlighted or emphasised in some way.
• Singapore | Hong Kong | Shanghai | Manila
• As we will soon open an office in Shanghai, having an option for both languages would be great.
Should not have
• I'm exceited and open to your creativity ... knock it out of the park!

```html
<!DOCTYPE html>
<html lang="en">
<head>
<meta charset="utf-8">
<title>Harbor Lending Circle – Business Card</title>
<link rel="stylesheet" href="https://fonts.googleapis.com/css2?family=Work+Sans:wght@400;500;600&display=swap">
<style>
  :root {
    --bg: #1b1b1c;
    --card: #232324;
    --card-edge: #2c2c2d;
    --ink: #f4f4f4;
    --accent: #2f6bd1;
  }
  * { box-sizing: border-box; margin: 0; padding: 0; }
  html, body { width: 1200px; height: 900px; overflow: hidden; }
  body {
    background: var(--bg);
    font-family: "Work Sans", Arial, sans-serif;
    color: var(--ink);
    display: flex;
    flex-direction: column;
    align-items: center;
    justify-content: center;
    gap: 40px;
  }
  .card {
    width: 700px;
    height: 400px;
    background: linear-gradient(135deg, var(--card) 0%, var(--card-edge) 100%);
    position: relative;
    box-shadow: 0 12px 30px rgba(0,0,0,.45);
  }
  .card-front { display: flex; flex-direction: column; align-items: center; justify-content: center; gap: 22px; }
  .brand-mark { width: 18px; height: 18px; background: var(--ink); }
  .brand-name {
    font-weight: 500;
    font-size: 34px;
    letter-spacing: 4px;
    text-transform: uppercase;
    color: var(--ink);
  }
  .person {
    position: absolute;
    right: 372px;
    top: 150px;
    text-align: right;
  }
  .person-name {
    color: var(--accent);
    font-weight: 600;
    font-size: 32px;
    letter-spacing: 1.5px;
    text-transform: uppercase;
    line-height: 1.1;
  }
  .person-title { font-size: 19px; letter-spacing: .5px; margin-top: 4px; }
  .divider {
    position: absolute;
    left: 350px;
    top: 150px;
    width: 2px;
    height: 96px;
    background: var(--accent);
  }
  .contacts {
    position: absolute;
    left: 374px;
    top: 150px;
    list-style: none;
    display: flex;
    flex-direction: column;
    gap: 4px;
  }
  .contacts li { display: flex; align-items: center; gap: 8px; font-size: 16px; line-height: 20px; }
  .contacts svg { width: 13px; height: 13px; flex: none; }
  .address {
    position: absolute;
    left: 0; right: 0;
    bottom: 48px;
    text-align: center;
    font-size: 19px;
    letter-spacing: .5px;
  }
</style>
</head>
<body>
  <section class="card card-front">
    <span class="brand-mark"></span>
    <h1 class="brand-name">Harbor Lending Circle</h1>
  </section>

  <section class="card card-back">
    <div class="person">
      <h2 class="person-name">Peter Wilks</h2>
      <p class="person-title">Co-Founder | Partner</p>
    </div>
    <span class="divider"></span>
    <ul class="contacts">
      <li>
        <svg viewBox="0 0 16 16" fill="none" stroke="var(--accent)" stroke-width="1.6"><path d="M4 1.5l2.5 3-1.5 1.8a9 9 0 004.7 4.7l1.8-1.5 3 2.5-1.5 2.5C7 14 2 9 1.5 3z"/></svg>
        +65 555-0142
      </li>
      <li>
        <svg viewBox="0 0 16 16" fill="none" stroke="var(--accent)" stroke-width="1.5"><rect x="1.5" y="3.5" width="13" height="9"/><path d="M1.5 3.5L8 9l6.5-5.5"/></svg>
        peterwilks@hlc-example.asia
      </li>
      <li>
        <svg viewBox="0 0 16 16" fill="none" stroke="var(--accent)" stroke-width="1.3"><circle cx="8" cy="8" r="6.5"/><ellipse cx="8" cy="8" rx="3" ry="6.5"/><path d="M1.5 8h13"/></svg>
        www.hlc-example.asia
      </li>
      <li>
        <svg viewBox="0 0 16 16"><circle cx="8" cy="8" r="6.5" fill="var(--accent)"/></svg>
        peterwilks
      </li>
    </ul>
    <p class="address">14 Cassia Lane, Suite 310 Singapore 047219</p>
  </section>
</body>
</html>
```